Brochure Design Project law firm

we require a print brochure for marketing. the information is contained on our website www.brindlecourt.com.au
we need to appeal to smash repairers who do third party claims. which means, where a person has had a car accident where it is not their fault they want their car fixed by the smash repairer who agrees to do the repairs and then claims the money from the insurer directly.

we will need a logo and business cards too.

Industry/Entity Type

Law Firm

Requirements
Must have
• pictures, law firm and smash repairer related.

```html
<!DOCTYPE html>
<html lang="en">
<head>
<meta charset="utf-8">
<title>Brindle Court – Tri-fold Brochure</title>
<link href="https://fonts.googleapis.com/css2?family=Arimo:wght@400;700&family=PT+Sans:wght@400;700&display=swap" rel="stylesheet">
<style>
:root{
  --canvas:#ffffff;
  --panel:#b4b4b4;
  --panel-dark:#6f6764;
  --ink:#1c1c1c;
  --red:#d0141b;
  --brand-red:#d51f26;
  --pill:#667170;
  --pill-ink:#2f3332;
  --link-blue:#1430d8;
}
*{margin:0;padding:0;box-sizing:border-box}
html,body{width:1200px;height:1005px;overflow:hidden;background:var(--canvas)}
body{position:relative;font-family:"Arimo",Arial,sans-serif;color:var(--ink)}
.sheet{position:absolute;left:250px;width:700px;height:490px;background:var(--panel);overflow:hidden}
.sheet--front{top:6px}
.sheet--back{top:509px}
.sheet__art{position:absolute;inset:0}
.panel{position:absolute;top:0;height:490px;width:233px}
.panel--1{left:0}.panel--2{left:233px}.panel--3{left:466px}
.abs{position:absolute}
.brand{color:var(--brand-red);font-weight:700;letter-spacing:.3px;white-space:nowrap}
.tagline{font-weight:700;color:var(--ink);white-space:nowrap}
.pill{position:absolute;background:var(--pill);color:var(--pill-ink);font-weight:700;font-size:17px;
  padding:3px 10px 4px;border-radius:12px;box-shadow:3px 3px 4px rgba(0,0,0,.45)}
.copy{position:absolute;font-size:9.6px;line-height:11.6px}
.copy p{margin-bottom:8px}
.copy--sans{font-family:"PT Sans",Arial,sans-serif;font-size:9.6px;line-height:12px}
.photo{position:absolute}
.banner-title{position:absolute;color:var(--link-blue);font-weight:700;font-size:14.5px;line-height:16px;text-align:center}
ul.copy{list-style:none}
ul.copy li::before{content:"•";margin-right:18px;margin-left:4px}
</style>
</head>
<body>

<section class="sheet sheet--front" aria-label="Brochure outside">
  <svg class="sheet__art" width="700" height="490" viewBox="0 0 700 490">
    <defs>
      <linearGradient id="headGrad" x1="0" x2="1">
        <stop offset="0" stop-color="#3b3330"/><stop offset=".6" stop-color="#8e8886"/><stop offset="1" stop-color="#ececec"/>
      </linearGradient>
      <linearGradient id="footGrad" x1="0" x2="1">
        <stop offset="0" stop-color="#3b3330"/><stop offset=".55" stop-color="#9a9492"/><stop offset="1" stop-color="#f4f4f4"/>
      </linearGradient>
    </defs>
    <rect x="466" y="58" width="234" height="412" fill="var(--panel-dark)"/>
    <rect x="233" y="84" width="233" height="126" fill="#8f8f8f"/>
    <rect x="0" y="0" width="233" height="58" fill="url(#headGrad)"/>
    <rect x="233" y="0" width="233" height="58" fill="url(#headGrad)"/>
    <rect x="466" y="0" width="234" height="58" fill="url(#headGrad)"/>
    <path d="M0 58 L0 52 L185 52 Q205 52 215 30 L228 0 L233 0 L233 58 Z" fill="var(--red)"/>
    <path d="M0 58 L0 54 L195 54 Q213 54 222 30 L233 2 L233 58 Z" fill="var(--panel)"/>
    <path d="M233 58 L233 52 L418 52 Q438 52 448 30 L461 0 L466 0 L466 58 Z" fill="var(--red)"/>
    <path d="M233 58 L233 56 L466 56 L466 58 Z" fill="#8f8f8f"/>
    <path d="M466 58 L466 52 L651 52 Q671 52 681 30 L694 0 L700 0 L700 58 Z" fill="var(--red)"/>
    <path d="M466 58 L466 56 L700 56 L700 58 Z" fill="var(--panel-dark)"/>
    <path d="M0 490 L0 455 Q40 490 140 480 L700 470 L700 490 Z" fill="url(#footGrad)"/>
    <path d="M0 455 Q40 490 140 480 L700 470 L700 476 L140 484 Q40 494 0 460 Z" fill="#e9a3a3"/>
    <path d="M233 468 L700 463 L700 470 L233 476 Z" fill="var(--red)"/>
    <path d="M640 463 L700 462 L700 469 L640 470 Z" fill="#111"/>
    <line x1="233" y1="0" x2="233" y2="478" stroke="#2a2a2a" stroke-width="1"/>
    <line x1="466" y1="0" x2="466" y2="478" stroke="#2a2a2a" stroke-width="1"/>
  </svg>

  <div class="panel panel--1">
    <div class="abs brand" style="left:20px;top:72px;font-size:19px">BRINDLE COURT</div>
    <div class="abs tagline" style="left:20px;top:103px;font-size:12.5px">THE RIGHT MOVE</div>
    <div class="pill" style="left:16px;top:162px">About Us</div>
    <div class="copy" style="left:14px;top:198px;width:212px">
      We focus on insurance claims for smash repairers in 3rd party claims. We fight the big insurers to ensure your rights are secured.<br>
      We assist smash repairers to make more money, find more work and improve levels of customer service for their clients.<br>
      We have state of the art systems and a team of dedicated professionals who will guide you every step of the way.<br>
      We only specialise in third party recovery claims<br>
      We act only in the best interests of Smash Repairers<br>
      We educate you in the legal process<br>
      We show you how to make more money and find more work<br>
      Our mission is to make a claim for a third party recovery as easy as possible to recover money from property damage insurers as quickly as possible.
    </div>
  </div>

  <div class="panel panel--2">
    <div class="photo" role="img" aria-label="Photo of stacked coins in front of a financial line chart"
      style="left:12px;top:82px;width:221px;height:110px;background:linear-gradient(135deg,#eef4fa 0%,#b9cfe2 45%,#7f97ad 75%,#d8e4ee 100%)"></div>
    <div class="pill" style="left:10px;top:222px">Results</div>
    <div class="copy copy--sans" style="left:12px;top:257px;width:215px">
      <p>We demand the best from our staff and obtain the best results for our clients.</p>
      <p style="margin-top:14px">Quick turnaround of claims so you can keep your cash flow strong. Ask us how</p>
    </div>
    <div class="pill" style="left:10px;top:340px">Contact</div>
    <div class="copy copy--sans" style="left:12px;top:380px;width:218px">
      Phone: 0400 318 522<br>
      Email: info@brindlecourt.com.au<br>
      Fax: 02 5550 0199<br>
      <span style="display:block;height:13px"></span>
      PO Box 4410 Harbour Square ASHVALE 2950<br>
      118 Kellerman Street, ASHVALE 2951
    </div>
  </div>

  <div class="panel panel--3">
    <div class="photo" role="img" aria-label="Banner photo of a young woman beside a pale blue background"
      style="left:0;top:145px;width:234px;height:70px;background:linear-gradient(90deg,#c9b8a8 0%,#e2d2c4 22%,#cfe6f5 40%,#eaf5fc 100%)"></div>
    <div class="banner-title" style="left:80px;top:157px;width:152px">What to Do After<br>a Car Crash</div>
    <div class="abs brand" style="left:5px;top:242px;font-size:37px;line-height:46px">BRINDLE<br>COURT</div>
    <div class="abs tagline" style="left:5px;top:429px;font-size:17px">THE RIGHT MOVE</div>
  </div>
</section>

<section class="sheet sheet--back" aria-label="Brochure inside">
  <svg class="sheet__art" width="700" height="490" viewBox="0 0 700 490">
    <defs>
      <linearGradient id="headGrad2" x1="0" x2="1">
        <stop offset="0" stop-color="#3b3330"/><stop offset=".6" stop-color="#8e8886"/><stop offset="1" stop-color="#ececec"/>
      </linearGradient>
      <linearGradient id="footGrad2" x1="0" x2="1">
        <stop offset="0" stop-color="#3b3330"/><stop offset=".55" stop-color="#9a9492"/><stop offset="1" stop-color="#f4f4f4"/>
      </linearGradient>
    </defs>
    <rect x="233" y="0" width="233" height="470" fill="var(--panel-dark)"/>
    <rect x="0" y="0" width="233" height="40" fill="url(#headGrad2)"/>
    <rect x="233" y="0" width="233" height="40" fill="url(#headGrad2)"/>
    <path d="M0 40 L0 34 L180 34 Q200 34 212 18 L226 0 L233 0 L233 40 Z" fill="var(--red)"/>
    <path d="M0 40 L0 37 L233 37 L233 40 Z" fill="var(--panel)"/>
    <path d="M233 40 L233 34 L410 34 Q432 34 444 18 L458 0 L466 0 L466 40 Z" fill="var(--red)"/>
    <path d="M233 40 L233 37 L466 37 L466 40 Z" fill="var(--panel-dark)"/>
    <path d="M0 490 L0 455 Q40 490 140 480 L700 470 L700 490 Z" fill="url(#footGrad2)"/>
    <path d="M0 455 Q40 490 140 480 L700 470 L700 476 L140 484 Q40 494 0 460 Z" fill="#e9a3a3"/>
    <path d="M233 468 L700 460 L700 467 L233 476 Z" fill="var(--red)"/>
    <path d="M640 461 L700 459 L700 466 L640 467 Z" fill="#111"/>
    <line x1="233" y1="0" x2="233" y2="478" stroke="#2a2a2a" stroke-width="1"/>
    <line x1="466" y1="0" x2="466" y2="478" stroke="#2a2a2a" stroke-width="1"/>
  </svg>

  <div class="panel panel--1">
    <div class="pill" style="left:14px;top:52px">Services</div>
    <div class="copy" style="left:14px;top:88px;width:210px">
      <p>We focus on 3rd party recovery for motor vehicle property damage claims. We fast track your claim to ensure the fastest turn around time. Our Ashvale head office is located in Kellerman street.</p>
      <p>We know how important a quick turn around in a claim is so you can do more repair work and keep your business going.</p>
      <p>We have state of the art systems and a team of dedicated professionals who will guide you every step of the way. We are small enough to ensure that you have personal service. We come to you.</p>
    </div>
    <div class="photo" role="img" aria-label="Photo of two cars after a rear-end collision on a roadway"
      style="left:12px;top:340px;width:212px;height:104px;background:linear-gradient(180deg,#d9dde0 0%,#a9b0b5 45%,#6d7479 100%)"></div>
  </div>

  <div class="panel panel--2">
    <div class="photo" role="img" aria-label="Photo of a presenter speaking to a seated business audience"
      style="left:14px;top:44px;width:212px;height:112px;background:linear-gradient(180deg,#f2f3f5 0%,#dfe2e6 50%,#9da4ad 100%)"></div>
    <div class="copy" style="left:14px;top:200px;width:212px;color:#1e1e1e">
      <p style="margin-bottom:2px">Call us today to benefit from:</p>
    </div>
    <ul class="copy" style="left:14px;top:214px;width:212px;color:#1e1e1e">
      <li>A proven track record</li>
      <li>Our committment to delivering an outstanding service to all of our clients</li>
    </ul>
    <div class="copy" style="left:14px;top:262px;width:212px;color:#1e1e1e">
      <p>If you want the best, call us on 0400 318 522 for a free, no obligation meeting with one of our specialist lawyers.<br>
      We take the fight the big insurers to achieve the best results and ensure your rights are secured.</p>
    </div>
  </div>

  <div class="panel panel--3">
    <div class="pill" style="left:14px;top:14px">Information</div>
    <div class="copy copy--sans" style="left:12px;top:50px;width:214px;font-size:9.2px;line-height:11.2px">
      <p>Do you have customers who ask if they can have their car repaired by you because you are known for quality and experience?</p>
      <p>What do you do when a client tells you that their insurer is telling them to take their car to another smash repairer because your quote is too high? We have a solution for you!</p>
      <p>If you send the repair estimate to your clients insurer, your clients insurer will not approve the repairs unless your hourly rate is lower than other smash repairers in your local area. For this reason you will receive a lower hourly rate to such an extent that it may become unprofitable for you to run your business or complete the job. As a result you may lose the work.</p>
      <p>Let us work for you!<br>We recovery money for a living. We threaten large insurance companies with the threat of litigation. We recover extremely good rates for our customers and pass on the savings. Try us today.<br>We can complete a claim within 6 weeks or we give you a discount.*</p>
      <p>*Conditions Apply - Please speak to one of our team who will explain the process.</p>
    </div>
    <div class="abs brand" style="left:60px;top:436px;font-size:17px">BRINDLE COURT</div>
  </div>
</section>

</body>
</html>
```